Hi,

Here are some thoughts on the book cover for The BRIGHT Wellness Map: A Restorative Vitality Path for Active Mothers and their Households.

To simplify this project I've uploaded some images (all images are of a vortex or swirl) that I would like to see the book cover design created with. I've also uploaded a set of "elements" that I would like to see incorporated into the vortex.

My vision is to have you infuse the smaller "elements" into the vortex so they look like they are caught in the vortex or swirling in the vortex.

I have upload an amateur example which I did but it shows the smaller elements dropped into the larger vortex image.

Please don't hesitate to write me with any questions you may have.

Thank you,

Gerald

Please.

Target Market(s)

Busy Women, both stay at home and career women

Industry/Entity Type

Health

Font styles to use
Serif
Sans Serif

Requirements
Must have
• vortex or swirl with circular elements infused

```html
<!DOCTYPE html>
<html lang="en">
<head>
<meta charset="utf-8">
<title>The BRIGHT Wellness Map — Book Cover</title>
<link rel="stylesheet" href="https://fonts.googleapis.com/css2?family=Cinzel:wght@400;500&family=Montserrat:wght@400&display=swap">
<style>
  :root {
    --paper: #ffffff;
    --haze: #eceef0;
    --ink: #1b1b1b;
    --title-green: #3e9b3c;
    --title-blue: #3b61b1;
    --title-magenta: #b3247e;
    --band: #00a8d2;
    --band-text: #ffffff;
    --swirl-blue: #2c63b8;
    --swirl-cyan: #28a6d6;
    --swirl-teal: #2fa87a;
    --swirl-lime: #a8cf3a;
  }
  * { margin: 0; padding: 0; box-sizing: border-box; }
  html, body { width: 800px; height: 1200px; overflow: hidden; background: var(--paper); }
  .cover {
    position: relative;
    width: 800px;
    height: 1200px;
    overflow: hidden;
    background: radial-gradient(ellipse 520px 360px at 50% 52%, var(--haze) 0%, var(--paper) 75%);
  }
  .title {
    position: absolute;
    top: 14px;
    left: 0;
    width: 100%;
    text-align: center;
    font-family: "Cinzel", "Trajan Pro", serif;
    font-weight: 400;
    line-height: 1;
  }
  .title span { display: block; }
  .title-the { font-size: 96px; color: var(--ink); height: 100px; }
  .title-bright { font-size: 124px; color: var(--title-green); height: 118px; }
  .title-wellness { font-size: 112px; color: var(--title-blue); height: 118px; letter-spacing: -1px; }
  .title-map { font-size: 124px; color: var(--title-magenta); height: 118px; }

  .vortex {
    position: absolute;
    left: 100px;
    top: 478px;
    width: 680px;
    height: 290px;
    border-radius: 48% 52% 40% 60% / 55% 45% 55% 45%;
    background: linear-gradient(100deg, var(--swirl-blue) 0%, var(--swirl-cyan) 35%, var(--swirl-teal) 62%, var(--swirl-lime) 100%);
    opacity: 0.85;
    transform: rotate(-8deg);
  }

  .subtitle {
    position: absolute;
    top: 840px;
    left: 0;
    width: 100%;
    text-align: center;
    font-family: "Cinzel", "Trajan Pro", serif;
    font-size: 42px;
    line-height: 50px;
    color: var(--ink);
  }

  .author-band {
    position: absolute;
    left: 0;
    bottom: 0;
    width: 100%;
    height: 140px;
    background: var(--band);
    display: flex;
    align-items: center;
    justify-content: center;
  }
  .author {
    font-family: "Montserrat", "Helvetica Neue", sans-serif;
    font-weight: 400;
    font-size: 58px;
    letter-spacing: 12px;
    padding-left: 12px;
    color: var(--band-text);
  }
</style>
</head>
<body>
  <main class="cover">
    <h1 class="title">
      <span class="title-the">THE</span>
      <span class="title-bright">BRIGHT</span>
      <span class="title-wellness">WELLNESS</span>
      <span class="title-map">MAP</span>
    </h1>

    <div class="vortex" role="img" aria-label="Flowing blue-to-green swirl of dotted ribbons with small circles caught in the vortex"></div>

    <p class="subtitle">
      A Restorative Vitality<br>
      Path for Active Mothers<br>
      and their Households
    </p>

    <footer class="author-band">
      <p class="author">GERALD</p>
    </footer>
  </main>
</body>
</html>
```